Landing Page that will convert (Design Only Landing Page Project)

I am looking for a design that will resonate with a dentist, doctor or anyone business owner in the medical field. My goal is to have then scheduled a 15 min session with me at the end to discuss how I can help then meet there financial goals (short or long term)

I am open to all design concepts and suggestions as far as the important contents or links that should be on the page (ie. Main menu like, Home, About, Services, Schedule, Contact Us).

There is no right or wrong answer, just need a great accounting/financing landing page. Again the project is for just the design of the page, and coding will be done elsewhere.

Target Market(s)

medical professionals, this includes small business owners of privately held office suck as medical doctors, dentist, ophthalmologist, chiropractors, etc

Industry/Entity Type

Finance And Accounting

Colors
fdfdfd
1b1b1b
f3f1f8
e4daeb

Requirements
Must have
• The goal of this landing page is to have the visitor schedule a 15min discovery call, therefore, a calender scheduling option is ideal, so we can understand their goals and see what obstacles they are facing and therefore avoid those obstacles before they become a burden
Nice to have
• A video background or maybe a medical professional office in that way they feel connected. For design purposes just use a video/image placeholder. I feel more is less if we can research some of the most successful landing page design and incorporate some of those elements that would to great.
• I saw this example and thought it was ok
• https://www.plovanet.com/#features
• WHAT I LIKE ABOUT THIS DESIGN:
• - It's simple, clean,
• - font is readable,
• - like the illustration
• - elegance
• - It clearly defines what the use should do, its intuitive, walks the user to the bottom of the page and give them the option of whether to signup or exit the page.

```html
<!DOCTYPE html>
<html lang="en">
<head>
<meta charset="utf-8">
<title>Fairleaf Finance — Finance Management for Medical Practices</title>
<link rel="stylesheet" href="https://fonts.googleapis.com/css2?family=Montserrat:wght@400;500;600;700&family=Lato:wght@400;700&display=swap">
<style>
:root{
  --white:#fdfdfd;
  --ink:#1b1b1b;
  --lilac-bg:#f3f1f8;
  --lilac:#e4daeb;
  --purple:#8e6fb5;
  --purple-mid:#6d4f91;
  --purple-dark:#4a2c63;
  --footer:#3e2352;
  --pink:#d46aa6;
  --grey:#6f6a75;
  --line:#d9d2e3;
}
*{box-sizing:border-box;margin:0;padding:0}
html,body{width:1200px;height:3888px;overflow:hidden}
body{position:relative;background:var(--white);font-family:"Lato",Arial,sans-serif;color:var(--ink);font-size:14px;line-height:1.6}
.abs{position:absolute}
h1,h2,h3,h4,.brand,.nav,.btn{font-family:"Montserrat",Arial,sans-serif}
.btn{display:inline-block;font-size:11px;font-weight:600;letter-spacing:.5px;text-transform:uppercase;padding:0 22px;height:38px;line-height:38px;border-radius:2px}
.btn-primary{background:var(--purple);color:#fff}
.btn-outline{border:1px solid var(--line);color:var(--purple-dark);background:#fff}
.brand{font-size:23px;font-weight:500;color:var(--purple-dark);letter-spacing:-.3px;display:flex;align-items:center;gap:9px}
.brand .mark{width:10px;height:10px;background:var(--purple)}

/* header */
.site-header{left:132px;top:22px;width:936px;height:42px;display:flex;align-items:center;justify-content:space-between;z-index:5}
.nav{display:flex;align-items:center;gap:34px;font-size:11px;font-weight:500;text-transform:uppercase;color:var(--grey)}
.nav .active{color:var(--ink)}
.nav .btn{color:#fff;height:40px;line-height:40px}

/* hero */
.hero-bg{left:0;top:0;width:1200px;height:560px;background:linear-gradient(180deg,#fff 0%,var(--lilac-bg) 100%)}
.hero-photo{left:540px;top:0;width:660px;height:520px;
  background:
    radial-gradient(ellipse 60% 50% at 70% 30%,rgba(255,255,255,.85) 0%,rgba(255,255,255,0) 70%),
    radial-gradient(ellipse 45% 35% at 55% 78%,rgba(120,132,160,.55) 0%,rgba(120,132,160,0) 70%),
    linear-gradient(135deg,#f1f3f8 0%,#dfe4ee 45%,#b8c2d4 100%);
  clip-path:polygon(12% 0,100% 0,100% 78%,76% 100%,30% 100%,0 50%)}
.hero-copy{left:132px;top:180px;width:400px}
.hero-copy h1{font-size:32px;font-weight:700;color:var(--purple-dark);line-height:1.25}
.hero-copy h1 span{display:block;font-weight:400;color:var(--purple)}
.hero-copy p{font-size:13px;color:var(--grey);margin:14px 0 28px;width:360px}
.hero-copy .btn+.btn{margin-left:12px}

/* sections */
.section-title{left:0;width:1200px;text-align:center}
.section-title h2{font-size:30px;font-weight:600;color:var(--purple-dark)}
.section-title p{width:620px;margin:14px auto 0;font-size:13px;color:var(--grey)}

.feature-card{width:203px;height:210px;background:#fff;box-shadow:0 6px 24px rgba(74,44,99,.1);text-align:center;padding-top:28px}
.feature-card h3{font-size:15px;font-weight:500;color:var(--purple-dark);line-height:1.4;margin-top:14px}

.service-card{width:283px;height:274px;background:#fff;box-shadow:0 6px 24px rgba(74,44,99,.08);text-align:center;padding:36px 28px 0}
.service-card h3{font-size:15px;font-weight:600;color:var(--purple-dark);margin:18px 0 10px}
.service-card p{font-size:12px;color:var(--grey);line-height:1.6}

/* about */
.about-bg{left:0;top:1860px;width:1200px;height:760px;background:linear-gradient(180deg,var(--white) 0%,var(--lilac-bg) 60%,var(--white) 100%)}
.about-copy{left:132px;top:2035px;width:370px}
.about-copy h2{font-size:31px;font-weight:600;color:var(--purple-dark);margin-bottom:20px}
.about-copy p{font-size:12.5px;color:var(--grey)}
.about-copy ul{list-style:none;margin:22px 0 30px}
.about-copy li{font-size:12.5px;color:var(--grey);padding-left:18px;position:relative;margin-bottom:10px}
.about-copy li::before{content:"›";position:absolute;left:0;color:var(--purple);font-weight:700}
.about-photo{left:590px;top:1950px;width:478px;height:560px;
  background:
    radial-gradient(ellipse 55% 40% at 50% 18%,rgba(250,246,238,.95) 0%,rgba(250,246,238,0) 75%),
    radial-gradient(ellipse 40% 30% at 35% 55%,rgba(196,170,146,.6) 0%,rgba(196,170,146,0) 75%),
    radial-gradient(ellipse 40% 30% at 68% 52%,rgba(245,245,248,.9) 0%,rgba(245,245,248,0) 75%),
    linear-gradient(180deg,#ece6dd 0%,#d8cfc4 55%,#f4f2ef 100%);
  clip-path:polygon(50% 0,100% 25%,100% 75%,50% 100%,0 75%,0 25%)}

/* testimonials */
.quote-card{width:315px;height:195px;background:#fff;box-shadow:0 6px 24px rgba(74,44,99,.1);padding:30px 30px 0}
.quote-card p{font-size:12px;color:var(--grey);line-height:1.6}
.stars{display:flex;gap:3px;margin-top:10px}
.person{display:flex;align-items:center;gap:14px}
.person .avatar{width:44px;height:44px;border-radius:50%;background:linear-gradient(135deg,#c9a58c,#7a5a48)}
.person h4{font-size:13px;font-weight:600;color:var(--purple-dark)}
.person span{font-size:10px;color:var(--grey)}
.clients-title{left:800px;top:2720px;width:300px}
.clients-title h2{font-size:31px;font-weight:600;color:var(--purple-dark);line-height:1.2}
.clients-title p{font-size:12.5px;color:var(--grey);margin-top:10px;width:230px}

/* schedule */
.schedule-copy{left:0;top:3090px;width:1200px;text-align:center;color:#fff}
.schedule-copy h2{font-size:31px;font-weight:600;margin-top:24px}
.schedule-copy p{width:600px;margin:10px auto 0;font-size:12.5px;color:#e7def0}
.schedule-form{left:330px;top:3300px;width:540px;display:grid;grid-template-columns:1fr 1fr;gap:16px 20px}
.field{height:40px;border:1px solid rgba(255,255,255,.45);border-radius:3px;font-size:11px;color:#eee3f5;padding:0 14px;display:flex;align-items:center;justify-content:space-between;font-family:"Montserrat",Arial,sans-serif}
.field.focus{background:#fff;color:var(--purple-dark);border-color:#fff}
.submit{left:537px;top:3472px;width:126px;height:38px;line-height:38px;background:#fff;color:var(--purple-dark);text-align:center;font-size:11px;font-weight:700;letter-spacing:.5px;border-radius:2px;font-family:"Montserrat",Arial,sans-serif}

/* footer */
.site-footer{left:0;top:3600px;width:1200px;height:288px;background:var(--footer);color:#cbbcd9}
.site-footer .brand{color:#fff;position:absolute;left:132px;top:62px}
.site-footer .brand .mark{background:#fff}
.footer-about{left:132px;top:115px;width:300px;font-size:12.5px}
.socials{left:132px;top:175px;display:flex;gap:10px}
.socials span{width:28px;height:28px;border:1px solid #a896b8;border-radius:50%;background:rgba(255,255,255,.1);display:flex;align-items:center;justify-content:center}
.socials span::after{content:"";width:8px;height:8px;border-radius:50%;background:#cbbcd9}
.copyright{left:132px;top:222px;font-size:11px;color:#9b8aac}
.footer-col{top:52px;font-size:12.5px}
.footer-col h4{color:#fff;font-size:13px;font-weight:600;margin-bottom:12px}
.footer-col li{list-style:none;margin-bottom:4px}
</style>
</head>
<body>

<div class="abs hero-bg"></div>
<svg class="abs" style="left:0;top:560px" width="1200" height="1330" viewBox="0 0 1200 1330" aria-hidden="true">
  <path d="M-60 60 L80 0 L240 80 L240 240 L80 320 L-60 260 Z" fill="none" stroke="#f0dfea" stroke-width="36" stroke-linejoin="round"/>
  <path d="M940 560 L1110 470 L1280 560 L1280 760 L1110 850 L940 760 Z" fill="none" stroke="#ece6f2" stroke-width="36" stroke-linejoin="round"/>
  <path d="M700 1330 L1200 980 L1200 1330 Z" fill="#f6f3f9"/>
</svg>

<div class="abs hero-photo" role="img" aria-label="Photo of a doctor in a white coat working on a laptop and calculator at a desk"></div>
<svg class="abs" style="left:500px;top:100px" width="260" height="400" viewBox="0 0 260 400" aria-hidden="true">
  <polygon points="18,6 26,10 26,20 18,24 10,20 10,10" fill="none" stroke="var(--purple)" stroke-width="1.5"/>
  <circle cx="60" cy="56" r="5" fill="none" stroke="var(--purple-dark)" stroke-width="2"/>
  <polygon points="100,300 116,309 116,327 100,336 84,327 84,309" fill="var(--purple-dark)"/>
  <polygon points="178,280 228,308 228,364 178,392 128,364 128,308" fill="var(--purple)"/>
  <circle cx="230" cy="396" r="5" fill="none" stroke="var(--purple-dark)" stroke-width="2"/>
</svg>

<header class="abs site-header">
  <div class="brand"><span class="mark"></span>Fairleaf Finance</div>
  <nav class="nav">
    <span class="active">Home</span><span>About</span><span>Services</span><span>Schedule</span><span>Contact Us</span>
    <span class="btn btn-primary">Scheduled a Session</span>
  </nav>
</header>

<section class="abs hero-copy">
  <h1>Finance Management <span>is heart of any business</span></h1>
  <p>Lorem ipsum dolor sit amet, consectetur adipiscing elit. Nullam in auctor urna.</p>
  <span class="btn btn-primary">Learn More</span><span class="btn btn-outline">View Services</span>
</section>

<div class="abs section-title" style="top:610px">
  <h2>Some of the Key Features</h2>
  <p>Lorem ipsum dolor sit amet, consectetur adipiscing elit. Nullam in auctor urna. Maecenas tempus lorem felis, vel mattis nisl viverra sit amet.</p>
</div>

<div class="abs feature-card" style="left:132px;top:757px">
  <svg width="90" height="90" viewBox="0 0 100 100"><polygon points="50,4 92,27 92,73 50,96 8,73 8,27" fill="var(--purple)"/><circle cx="50" cy="50" r="17" fill="none" stroke="#fff" stroke-width="2.5"/><ellipse cx="50" cy="50" rx="7" ry="17" fill="none" stroke="#fff" stroke-width="2"/><path d="M33 50h34M36 41h28M36 59h28" stroke="#fff" stroke-width="2"/></svg>
  <h3>Expand<br>Your Reach</h3>
</div>
<div class="abs feature-card" style="left:377px;top:757px">
  <svg width="90" height="90" viewBox="0 0 100 100"><polygon points="50,4 92,27 92,73 50,96 8,73 8,27" fill="var(--purple-dark)"/><path d="M34 66h34M38 64V56M46 64V50M54 64V46M62 64V40M36 50l12-10 8 6 12-12" fill="none" stroke="#fff" stroke-width="2.5"/></svg>
  <h3>Higher Annualized<br>Growth Rate</h3>
</div>
<div class="abs feature-card" style="left:620px;top:757px">
  <svg width="90" height="90" viewBox="0 0 100 100"><polygon points="50,4 92,27 92,73 50,96 8,73 8,27" fill="var(--pink)"/><rect x="36" y="34" width="28" height="34" rx="2" fill="none" stroke="#fff" stroke-width="2.5"/><path d="M44 32h12v6H44zM50 44v12M44 50h12" fill="none" stroke="#fff" stroke-width="2.5"/></svg>
  <h3>Manage<br>Your Patients</h3>
</div>
<div class="abs feature-card" style="left:865px;top:757px">
  <svg width="90" height="90" viewBox="0 0 100 100"><polygon points="50,4 92,27 92,73 50,96 8,73 8,27" fill="var(--purple-dark)"/><circle cx="50" cy="53" r="16" fill="none" stroke="#fff" stroke-width="2.5"/><path d="M50 53V44M50 53l7 4M46 33h8M50 33v4" fill="none" stroke="#fff" stroke-width="2.5"/></svg>
  <h3>Track<br>Your Time</h3>
</div>

<div class="abs section-title" style="top:1060px">
  <h2>Our Services</h2>
  <p>Lorem ipsum dolor sit amet, consectetur adipiscing elit. Nullam in auctor urna. Maecenas tempus lorem felis, vel mattis nisl viverra sit amet.</p>
</div>

<div class="abs service-card" style="left:132px;top:1208px">
  <svg width="84" height="84" viewBox="0 0 100 100"><polygon points="50,4 92,27 92,73 50,96 8,73 8,27" fill="var(--lilac-bg)"/><rect x="36" y="30" width="28" height="38" rx="2" fill="none" stroke="var(--purple)" stroke-width="2"/><path d="M42 40h16M42 47h16M42 54h10" stroke="var(--purple)" stroke-width="2"/></svg>
  <h3>Invoice and Quotes</h3>
  <p>Lorem ipsum dolor sit amet, consectetur adipiscing elit. Nullam in auctor urna. Maecenas tempus lorem felis.</p>
</div>
<div class="abs service-card" style="left:459px;top:1208px">
  <svg width="84" height="84" viewBox="0 0 100 100"><polygon points="50,4 92,27 92,73 50,96 8,73 8,27" fill="var(--lilac-bg)"/><path d="M32 42l18-10 18 10zM34 66h32M36 46v16M44 46v16M56 46v16M64 46v16" fill="none" stroke="var(--purple-dark)" stroke-width="2"/></svg>
  <h3>Bank Reconciliation</h3>
  <p>Lorem ipsum dolor sit amet, consectetur adipiscing elit. Nullam in auctor urna. Maecenas tempus lorem felis.</p>
</div>
<div class="abs service-card" style="left:784px;top:1208px">
  <svg width="84" height="84" viewBox="0 0 100 100"><polygon points="50,4 92,27 92,73 50,96 8,73 8,27" fill="var(--lilac-bg)"/><rect x="32" y="38" width="36" height="28" rx="3" fill="none" stroke="var(--pink)" stroke-width="2"/><path d="M44 38v-5h12v5M50 45v14M43 52h14" fill="none" stroke="var(--pink)" stroke-width="2"/></svg>
  <h3>Inventory</h3>
  <p>Lorem ipsum dolor sit amet, consectetur adipiscing elit. Nullam in auctor urna. Maecenas tempus lorem felis.</p>
</div>
<div class="abs service-card" style="left:132px;top:1521px">
  <svg width="84" height="84" viewBox="0 0 100 100"><polygon points="50,4 92,27 92,73 50,96 8,73 8,27" fill="var(--lilac-bg)"/><path d="M32 58l10-8h12l8 6M68 44l-10 8H46M40 40h14" fill="none" stroke="var(--purple-dark)" stroke-width="2"/><circle cx="58" cy="36" r="5" fill="none" stroke="var(--purple)" stroke-width="2"/></svg>
  <h3>Pay your Employees</h3>
  <p>Lorem ipsum dolor sit amet, consectetur adipiscing elit. Nullam in auctor urna. Maecenas tempus lorem felis.</p>
</div>
<div class="abs service-card" style="left:459px;top:1521px">
  <svg width="84" height="84" viewBox="0 0 100 100"><polygon points="50,4 92,27 92,73 50,96 8,73 8,27" fill="var(--lilac-bg)"/><rect x="36" y="30" width="28" height="40" rx="2" fill="none" stroke="var(--purple-dark)" stroke-width="2"/><path d="M42 40h16M42 48h16M42 56h8M54 60h6" stroke="var(--purple)" stroke-width="2"/></svg>
  <h3>Enter Bills</h3>
  <p>Lorem ipsum dolor sit amet, consectetur adipiscing elit. Nullam in auctor urna. Maecenas tempus lorem felis.</p>
</div>
<div class="abs service-card" style="left:784px;top:1521px">
  <svg width="84" height="84" viewBox="0 0 100 100"><polygon points="50,4 92,27 92,73 50,96 8,73 8,27" fill="var(--lilac-bg)"/><rect x="38" y="30" width="24" height="38" fill="none" stroke="#5aa8b0" stroke-width="2"/><path d="M44 38h4M52 38h4M44 46h4M52 46h4M44 54h4M52 54h4M47 68v-7h6v7" fill="none" stroke="#5aa8b0" stroke-width="2"/></svg>
  <h3>Manage your Patients</h3>
  <p>Lorem ipsum dolor sit amet, consectetur adipiscing elit. Nullam in auctor urna. Maecenas tempus lorem felis.</p>
</div>

<div class="abs about-bg"></div>
<section class="abs about-copy">
  <h2>Who we are?</h2>
  <p>Lorem ipsum dolor sit amet, consectetur adipiscing elit. Nullam in auctor urna. Maecenas tempus lorem felis, vel mattis nisl viverra sit amet. Pellentesque in diam et dui condimentum fringilla.</p>
  <ul>
    <li>Lorem ipsum dolor sit amet, consectetur adipiscing elit. Nullam in auctor urna.</li>
    <li>Maecenas tempus lorem felis, vel mattis nisl viverra sit amet.</li>
    <li>Pellentesque in diam et dui condimentum fringilla.</li>
    <li>Nunc mauris libero, dignissim in orci tincidunt</li>
  </ul>
  <span class="btn btn-primary">Learn More</span>
</section>
<div class="abs about-photo" role="img" aria-label="Photo of a financial advisor and a doctor reviewing figures on a laptop in a bright office"></div>
<svg class="abs" style="left:535px;top:2060px" width="240" height="470" viewBox="0 0 240 470" aria-hidden="true">
  <polygon points="18,6 32,14 32,30 18,38 4,30 4,14" fill="var(--purple-dark)"/>
  <polygon points="112,296 160,322 160,374 112,400 64,374 64,322" fill="var(--purple)"/>
  <polygon points="204,432 218,440 218,456 204,464 190,456 190,440" fill="none" stroke="var(--purple-dark)" stroke-width="3"/>
  <polygon points="204,440 211,444 211,452 204,456 197,452 197,444" fill="var(--purple)"/>
</svg>

<div class="abs quote-card" style="left:-280px;top:2665px"></div>
<div class="abs quote-card" style="left:80px;top:2665px">
  <p>Mauris rutrum justo justo, quis vestibulum ligula facilisis id. In pellentesque imperdiet nisl ut bibendum. Nunc malesuada felis vel tincidunt molestie. In tristique ante id dictum pulvinar.</p>
  <div class="stars"><svg width="80" height="14" viewBox="0 0 80 14"><g fill="none" stroke="var(--purple)"><path id="st" d="M7 1l1.8 3.8 4.2.5-3 2.9.8 4.1L7 10.3l-3.8 2 .8-4.1-3-2.9 4.2-.5z"/><use href="#st" x="16"/><use href="#st" x="32"/><use href="#st" x="48"/><use href="#st" x="64"/></g></svg></div>
</div>
<div class="abs quote-card" style="left:430px;top:2665px">
  <p>Mauris rutrum justo justo, quis vestibulum ligula facilisis id. In pellentesque imperdiet nisl ut bibendum. Nunc malesuada felis vel tincidunt molestie. In tristique ante id dictum pulvinar.</p>
  <div class="stars"><svg width="80" height="14" viewBox="0 0 80 14"><g fill="none" stroke="var(--purple)"><use href="#st"/><use href="#st" x="16"/><use href="#st" x="32"/><use href="#st" x="48"/><use href="#st" x="64"/></g></svg></div>
</div>
<div class="abs person" style="left:84px;top:2878px"><span class="avatar" role="img" aria-label="Client portrait"></span><div><h4>Daniel Reyes</h4><span>Senior Dr. at Lakeview Clinic</span></div></div>
<div class="abs person" style="left:434px;top:2878px"><span class="avatar" role="img" aria-label="Client portrait"></span><div><h4>Daniel Reyes</h4><span>Senior Dr. at Lakeview Clinic</span></div></div>
<svg class="abs" style="left:800px;top:2662px" width="62" height="48" viewBox="0 0 62 48" aria-hidden="true"><path d="M0 48V26C0 10 8 2 24 0v9c-8 2-11 6-11 13h11v26zM38 48V26C38 10 46 2 62 0v9c-8 2-11 6-11 13h11v26z" fill="var(--lilac)"/></svg>
<div class="abs clients-title">
  <h2>What our clients are saying</h2>
  <p>Lorem ipsum dolor sit amet, consectetur adipiscing elit.</p>
</div>

<svg class="abs" style="left:0;top:2990px" width="1200" height="610" viewBox="0 0 1200 610" aria-hidden="true">
  <defs><linearGradient id="sg" x1="0" y1="0" x2="1" y2="1"><stop offset="0" stop-color="#5b3c7a"/><stop offset="1" stop-color="#8a6bb2"/></linearGradient></defs>
  <path d="M0 330 L540 20 Q600 -12 660 20 L1200 330 V610 H0 Z" fill="url(#sg)"/>
  <path d="M740 360 L850 300 L960 360 L960 480 L850 540 L740 480 Z" fill="none" stroke="rgba(255,255,255,.06)" stroke-width="26"/>
</svg>
<section class="abs schedule-copy">
  <svg width="60" height="60" viewBox="0 0 60 60" aria-hidden="true"><rect x="8" y="12" width="44" height="40" rx="4" fill="none" stroke="#fff" stroke-width="2.5"/><path d="M8 22h44M19 6v10M41 6v10" stroke="#fff" stroke-width="2.5"/><g fill="#fff"><circle cx="18" cy="31" r="2"/><circle cx="26" cy="31" r="2"/><circle cx="34" cy="31" r="2"/><circle cx="42" cy="31" r="2"/><circle cx="18" cy="40" r="2"/><circle cx="26" cy="40" r="2"/><circle cx="34" cy="40" r="2"/></g></svg>
  <h2>Scheduled A 15 Minutes Session</h2>
  <p>Lorem ipsum dolor sit amet, consectetur adipiscing elit. Nullam in auctor urna. Maecenas tempus lorem felis, vel mattis nisl viverra sit amet.</p>
</section>
<form class="abs schedule-form">
  <div class="field focus">First Name</div>
  <div class="field">Last Name</div>
  <div class="field">Email Addres</div>
  <div class="field">Phone</div>
  <div class="field">Choose Session Date <svg width="14" height="14" viewBox="0 0 14 14"><rect x="1" y="2" width="12" height="11" fill="none" stroke="#eee3f5"/><path d="M1 5h12" stroke="#eee3f5"/></svg></div>
  <div class="field">Choose Session Time <svg width="14" height="14" viewBox="0 0 14 14"><circle cx="7" cy="7" r="6" fill="none" stroke="#eee3f5"/><path d="M7 3.5V7l2.5 1.5" fill="none" stroke="#eee3f5"/></svg></div>
</form>
<div class="abs submit">SUBMIT NOW</div>

<footer class="abs site-footer">
  <div class="brand"><span class="mark"></span>Fairleaf Finance</div>
  <p class="abs footer-about">Mauris rutrum justo justo, quis vestibulum ligula facilisis id. In pellentesque.</p>
  <div class="abs socials" aria-label="Social links"><span></span><span></span><span></span><span></span></div>
  <p class="abs copyright">2018 © Copyright Fairleaf Finance. All Rights Reserved.</p>
  <div class="abs footer-col" style="left:528px"><h4>Services</h4><ul><li>Lorem ipsum dolor</li><li>Nullam in auctor</li><li>Maecenas tempus</li><li>Pellentesque in diam</li></ul></div>
  <div class="abs footer-col" style="left:772px"><h4>Company</h4><ul><li>The Team</li><li>About Us</li><li>Blog</li><li>Press</li></ul></div>
  <div class="abs footer-col" style="left:966px"><h4>Resources</h4><ul><li>Support</li><li>Contact</li><li>Cookies</li><li>Terms of Services</li></ul></div>
</footer>

</body>
</html>
```